Premium Audio and HD Video with HLM!

HLM is a mobile studio that provides premium audio and HD video recording for the classical and jazz community in the Boston area. Specializing in concerts, recitals, auditions, studio releases, lectures, podcasts and more.
My website:
http://harborlanternmedia.example
https://www.facebook.com/HLMediaworks/
Target Market(s)
classical and jazz instrumentalists, vocalists, ensembles, choruses, a cappella groups, podcasters
Industry/Entity Type
Audio
Font styles to use
Serif
Colors
Designer to choose colors to be used in the design.
Requirements
Must have
- My logo!
- Must convey that this mobile recording studio is for classical and jazz musicians... not rock bands etc.
- I provide event recording as well as "studio recording" (for CDs etc)
- Eye catching
- Must be scalable for different size flyers... full page, half page etc
- I will use it for bulletin boards.. so the front side is most important... if the design is two sided, the lesser important info should be on the back side.
Nice to have
- Use some of the photos on my facebook page? Not sure they are high res or decent photos..
- https://www.facebook.com/HLMediaworks/
Should not have
- Anything depicting a rock band or similar

```html
<!DOCTYPE html>
<html lang="en">
<head>
<meta charset="utf-8">
<title>Harbor Lantern Media – Mobile Recording Flyer</title>
<link rel="stylesheet" href="https://fonts.googleapis.com/css2?family=Alfa+Slab+One&family=Courier+Prime:wght@400;700&display=swap">
<style>
  :root {
    --page-bg: #ffffff;
    --studio-light: #8f8b8c;
    --studio-dark: #5e5a5b;
    --mic-steel: #3c3b3d;
    --mic-shine: #a9a8ab;
    --skin: #d7a58c;
    --hair: #b08a5c;
    --panel: #3a3a3a;
    --panel-edge: #2f2f2f;
    --mint: #d6ecdd;
    --ink: #f1f1f1;
    --green: #3fe03a;
    --frame: #b9b9b9;
  }
  * { box-sizing: border-box; margin: 0; padding: 0; }
  html, body { width: 800px; height: 1200px; overflow: hidden; background: var(--page-bg); }
  .flyer {
    position: relative; width: 800px; height: 1200px; overflow: hidden;
    font-family: "Courier Prime", "Courier New", monospace; color: var(--ink);
    background: var(--panel);
  }
  .hero-photo {
    position: absolute; left: 0; top: 0; width: 800px; height: 612px;
    background:
      radial-gradient(ellipse 230px 280px at 640px 330px, rgba(215,165,140,0.95) 0%, rgba(176,138,92,0.75) 45%, rgba(176,138,92,0) 100%),
      radial-gradient(ellipse 140px 170px at 690px 190px, rgba(176,138,92,0.8) 0%, rgba(176,138,92,0) 100%),
      linear-gradient(90deg, rgba(60,59,61,0) 90px, rgba(60,59,61,0.85) 130px, rgba(169,168,171,0.85) 170px, rgba(60,59,61,0.9) 215px, rgba(60,59,61,0) 250px),
      radial-gradient(ellipse at 45% 40%, var(--studio-light) 0%, var(--studio-dark) 100%);
  }
  .brand-mark {
    position: absolute; left: 270px; top: 70px; width: 270px; text-align: center;
    font-weight: 700; color: var(--ink); font-size: 30px; line-height: 1.1;
  }
  .brand-mark small { display: block; font-size: 14px; letter-spacing: 6px; font-weight: 700; }
  .headline {
    position: absolute; left: 0; width: 800px; top: 515px; text-align: center;
    font-family: "Alfa Slab One", Georgia, serif; font-size: 64px; line-height: 1;
    color: var(--mint); letter-spacing: -1px;
  }
  .info-panel {
    position: absolute; left: 0; top: 604px; width: 800px; height: 596px;
    background: linear-gradient(180deg, var(--panel) 0%, var(--panel-edge) 100%);
  }
  .pitch {
    position: absolute; left: 50px; top: 28px; width: 720px;
    font-weight: 700; font-size: 26px; line-height: 1.3; white-space: nowrap;
  }
  .accent { color: var(--green); }
  .service-line { position: absolute; left: 50px; top: 118px; font-size: 16px; font-weight: 700; white-space: nowrap; }
  .service-line .accent { font-size: 24px; }
  .community { position: absolute; left: 50px; top: 178px; font-size: 16px; line-height: 1.35; font-weight: 700; }
  .services-title { position: absolute; left: 50px; top: 246px; font-size: 14px; color: var(--green); font-weight: 700; }
  .service-list { position: absolute; left: 50px; top: 290px; list-style: none; }
  .service-list li { display: flex; align-items: center; gap: 12px; height: 26px; font-size: 13px; font-weight: 700; }
  .tick { width: 12px; height: 12px; }
  .ensemble-photo {
    position: absolute; left: 352px; top: 278px; width: 400px; height: 186px;
    border: 5px solid var(--frame);
    background: linear-gradient(180deg, #e4e2dc 0%, #b5b0a6 30%, #2d2a28 55%, #3a3532 82%, #c9a25a 100%);
  }
  .contact { position: absolute; left: 50px; top: 506px; list-style: none; }
  .contact li { display: flex; align-items: center; gap: 12px; height: 22px; font-size: 13px; }
  .contact svg { width: 14px; height: 14px; }
  .signature { position: absolute; left: 536px; top: 508px; font-size: 20px; font-weight: 700; line-height: 1.35; }
</style>
</head>
<body>
<main class="flyer">
  <div class="hero-photo" role="img" aria-label="Singer in headphones performing at a studio condenser microphone"></div>
  <div class="brand-mark">Harbor Lantern<small>MEDIA</small></div>
  <h1 class="headline">HARBOR LANTERN</h1>

  <section class="info-panel">
    <p class="pitch">MOBILE RECORDING STUDIO IS FOR CLASSICAL<br>AND JAZZ MUSICIANS... <span class="accent">NOT ROCK BANDS ETC.</span></p>
    <p class="service-line">I PROVIDE EVENT RECORDING AS WELL AS <span class="accent">"STUDIO RECORDING"</span></p>
    <p class="community">SERVING THE SOLO VOCAL/INSTRUMENTAL, CHAMBER MUSIC,<br>CHORAL, ORCHESTRAL, AND CONTEMPORARY ACAPPELLA COMMUNITIES</p>
    <p class="services-title">PROVIDES AUDIO AND VIDEO PRODUCTION SERVICES FOR</p>
    <ul class="service-list">
      <li><svg class="tick" viewBox="0 0 12 12"><circle cx="6" cy="6" r="6" fill="#f1f1f1"/><path d="M3 6.2l2 2 4-4.4" stroke="#3a3a3a" stroke-width="1.6" fill="none"/></svg>CONCERTS</li>
      <li><svg class="tick" viewBox="0 0 12 12"><circle cx="6" cy="6" r="6" fill="#f1f1f1"/><path d="M3 6.2l2 2 4-4.4" stroke="#3a3a3a" stroke-width="1.6" fill="none"/></svg>RECITALS</li>
      <li><svg class="tick" viewBox="0 0 12 12"><circle cx="6" cy="6" r="6" fill="#f1f1f1"/><path d="M3 6.2l2 2 4-4.4" stroke="#3a3a3a" stroke-width="1.6" fill="none"/></svg>STUDIO RELEASES</li>
      <li><svg class="tick" viewBox="0 0 12 12"><circle cx="6" cy="6" r="6" fill="#f1f1f1"/><path d="M3 6.2l2 2 4-4.4" stroke="#3a3a3a" stroke-width="1.6" fill="none"/></svg>AUDITIONS</li>
      <li><svg class="tick" viewBox="0 0 12 12"><circle cx="6" cy="6" r="6" fill="#f1f1f1"/><path d="M3 6.2l2 2 4-4.4" stroke="#3a3a3a" stroke-width="1.6" fill="none"/></svg>LECTURES</li>
      <li><svg class="tick" viewBox="0 0 12 12"><circle cx="6" cy="6" r="6" fill="#f1f1f1"/><path d="M3 6.2l2 2 4-4.4" stroke="#3a3a3a" stroke-width="1.6" fill="none"/></svg>PODCASTS &amp; MORE</li>
    </ul>
    <div class="ensemble-photo" role="img" aria-label="Choir and orchestra performing on a concert stage"></div>
    <ul class="contact">
      <li><svg viewBox="0 0 14 14"><path d="M2 4c0-1.5 1.5-2.5 5-2.5S12 2.5 12 4v1.2H9.5V4h-5v1.2H2z M3.5 6.5h7l1.5 5.5H2z" fill="#f1f1f1"/></svg>555.010.4827</li>
      <li><svg viewBox="0 0 14 14"><rect x="1" y="3" width="12" height="8" fill="#f1f1f1"/><path d="M1 3l6 5 6-5" stroke="#3a3a3a" stroke-width="1.2" fill="none"/></svg>dan@harborlanternmedia.example</li>
      <li><svg viewBox="0 0 14 14"><circle cx="7" cy="7" r="6" fill="#f1f1f1"/><path d="M1 7h12M7 1v12" stroke="#3a3a3a" stroke-width="1.1"/></svg>harborlanternmedia.example</li>
    </ul>
    <p class="signature">Daniel Rourke<br><span class="accent">Principal Engineer</span></p>
  </section>
</main>
</body>
</html>
```